Solar appointment reminder card

We are looking for a new design for our appointment reminder card since we have changed our logo. The card should have the new logo along with space for the employee to hand write the customers appointment date, time, the employees name and phone number.
I've uploaded what our old basic appointment card looked like and our new logo.

The cards should be in a standard business card size and could be horizontal or vertical.

```html
<!DOCTYPE html>
<html lang="en">
<head>
<meta charset="utf-8">
<title>Quillmore Solar – Appointment Card</title>
<link href="https://fonts.googleapis.com/css2?family=Open+Sans:wght@400;800&display=swap" rel="stylesheet">
<style>
  :root {
    --page-bg: #e9e6e1;
    --card-bg: #ffffff;
    --ink: #454545;
    --accent: #f28c1e;
    --accent-light: #fbb040;
    --panel-deep: #1d4aa3;
    --panel-mid: #2f6fc6;
    --sky: #3f9fe0;
    --sky-pale: #cfe8f7;
  }
  html, body {
    margin: 0;
    padding: 0;
    width: 857px;
    height: 1200px;
    overflow: hidden;
    background: var(--page-bg);
    font-family: "Open Sans", Arial, sans-serif;
  }
  .appointment-card {
    position: absolute;
    left: 48px;
    top: 383px;
    width: 760px;
    height: 433px;
    background: var(--card-bg);
    overflow: hidden;
    box-shadow: 0 2px 10px rgba(0,0,0,0.12);
  }
  .solar-visual {
    position: absolute;
    inset: 0;
    background:
      linear-gradient(90deg, rgba(255,255,255,0) 0%, rgba(255,255,255,0) 30%, rgba(255,255,255,0.6) 46%, rgba(255,255,255,0.95) 56%, #fff 60%),
      linear-gradient(165deg, var(--sky) 0%, var(--sky-pale) 30%, var(--panel-mid) 48%, var(--panel-deep) 78%, #2a5cb5 100%);
  }
  .brand {
    position: absolute;
    left: 20px;
    top: 204px;
    display: flex;
    align-items: center;
    gap: 10px;
    white-space: nowrap;
  }
  .brand-dot {
    width: 26px;
    height: 26px;
    border-radius: 50%;
    background: var(--accent);
  }
  .brand-name {
    font-weight: 800;
    font-size: 28px;
    line-height: 1;
    color: var(--accent);
  }
  .card-title {
    position: absolute;
    left: 384px;
    top: 48px;
    margin: 0;
    font-weight: 800;
    font-size: 43px;
    line-height: 1.1;
    color: var(--ink);
    white-space: nowrap;
  }
  .title-marker {
    position: absolute;
    left: 735px;
    top: 59px;
    width: 25px;
    height: 36px;
    background: var(--accent);
  }
  .detail-list {
    position: absolute;
    left: 376px;
    top: 0;
    margin: 0;
    padding: 0;
    list-style: none;
  }
  .detail-row {
    position: absolute;
    left: 0;
    display: flex;
    align-items: center;
    white-space: nowrap;
  }
  .detail-icon {
    width: 40px;
    height: 40px;
    border-radius: 50%;
    background: radial-gradient(circle at 40% 35%, var(--accent-light), var(--accent));
    box-shadow: 0 2px 4px rgba(0,0,0,0.25);
    display: flex;
    align-items: center;
    justify-content: center;
    margin-right: 11px;
  }
  .detail-icon svg { width: 22px; height: 22px; }
  .detail-label {
    font-size: 21px;
    color: var(--ink);
  }
  .row-date { top: 137px; }
  .row-time { top: 196px; }
  .row-rep { top: 259px; }
  .row-phone { top: 324px; }
</style>
</head>
<body>
  <main class="appointment-card">
    <div class="solar-visual" role="img" aria-label="Photograph of rooftop solar panels under a clear blue sky, fading to white"></div>

    <div class="brand">
      <span class="brand-dot"></span>
      <span class="brand-name">Quillmore Solar</span>
    </div>

    <h1 class="card-title">APPOINTMENT</h1>
    <span class="title-marker"></span>

    <ul class="detail-list">
      <li class="detail-row row-date">
        <span class="detail-icon">
          <svg viewBox="0 0 24 24" fill="none" stroke="#fff" stroke-width="2">
            <rect x="3" y="5" width="16" height="15" rx="1.5"/>
            <line x1="3" y1="10" x2="19" y2="10"/>
            <line x1="8" y1="3" x2="8" y2="7"/>
            <line x1="14" y1="3" x2="14" y2="7"/>
          </svg>
        </span>
        <span class="detail-label">Date:</span>
      </li>
      <li class="detail-row row-time">
        <span class="detail-icon">
          <svg viewBox="0 0 24 24" fill="none" stroke="#fff" stroke-width="2">
            <circle cx="12" cy="12" r="8.5"/>
            <polyline points="12,7 12,12 15.5,14"/>
          </svg>
        </span>
        <span class="detail-label">Time:</span>
      </li>
      <li class="detail-row row-rep">
        <span class="detail-icon">
          <svg viewBox="0 0 24 24" fill="#fff">
            <circle cx="12" cy="8" r="4"/>
            <path d="M4 21c0-4.5 3.5-7.5 8-7.5s8 3 8 7.5z"/>
          </svg>
        </span>
        <span class="detail-label">Representative:</span>
      </li>
      <li class="detail-row row-phone">
        <span class="detail-icon">
          <svg viewBox="0 0 24 24" fill="#fff">
            <path d="M6.6 10.8a15 15 0 0 0 6.6 6.6l2.2-2.2a1 1 0 0 1 1-.25 11.4 11.4 0 0 0 3.6.57 1 1 0 0 1 1 1V20a1 1 0 0 1-1 1A17 17 0 0 1 3 4a1 1 0 0 1 1-1h3.5a1 1 0 0 1 1 1c0 1.25.2 2.45.57 3.57a1 1 0 0 1-.25 1z"/>
          </svg>
        </span>
        <span class="detail-label">Phone:</span>
      </li>
    </ul>
  </main>
</body>
</html>
```